Kestrel Valley Alpine Riders Society needs a business card design

We need a business card design for our newly incorporated KVARS. We are helping the NZ Chinese community, as well as everyone else, to organise ski & snowboarding trips, training, and equipments. The design should be creative, energetic, young and vibrant.

Industry/Entity Type

Social Club

Contact Information for Business Card

Logo; Kestrel Valley Alpine Riders Society; Name: Oliver Brandt; Position: President; Address: 42 Marwick Rd, Epsom, Auckland 1051; Mobile: 020 7826 1957; Email: oliver@kvars-club.example; Web: www.kvars-club.example

Requirements
Must have
• 1, The text "Kestrel Valley Alpine Riders Society" should be put together with the supplied logo file to form a new complete logo combination.
• 2, Final design files should be in Adobe Illustrator format and all text must be editable.
Nice to have
• two or three colours

```html
<!DOCTYPE html>
<html lang="en">
<head>
<meta charset="utf-8">
<title>Kestrel Valley Alpine Riders Society – Business Card</title>
<link rel="stylesheet" href="https://fonts.googleapis.com/css2?family=Montserrat:wght@600;800&family=Roboto:wght@400;500&display=swap">
<style>
  :root {
    --page: #cccccc;
    --card: #fafafa;
    --navy: #1d3a5f;
    --brand-blue: #1565c0;
    --ink: #3a3f47;
  }
  * { box-sizing: border-box; margin: 0; padding: 0; }
  html, body { width: 1200px; height: 1005px; overflow: hidden; }
  body {
    background: var(--page);
    display: flex;
    flex-direction: column;
    align-items: center;
    justify-content: center;
    gap: 44px;
    font-family: "Roboto", Arial, sans-serif;
  }
  .card {
    position: relative;
    width: 760px;
    height: 440px;
    background: var(--card);
    box-shadow: 0 6px 14px rgba(0,0,0,0.18);
  }
  .brand {
    position: absolute;
    display: flex;
    flex-direction: column;
    align-items: center;
  }
  .wordmark {
    display: flex;
    align-items: center;
    gap: 14px;
    font-family: "Montserrat", Arial, sans-serif;
    font-weight: 800;
    color: var(--brand-blue);
    line-height: 1;
  }
  .wordmark .mark-dot {
    border-radius: 50%;
    background: var(--brand-blue);
  }
  .society-name {
    font-family: "Montserrat", Arial, sans-serif;
    font-weight: 800;
    color: var(--brand-blue);
    text-transform: uppercase;
    white-space: nowrap;
  }
  .card-front .brand {
    left: 50%;
    top: 50%;
    transform: translate(-50%, -50%);
  }
  .card-front .wordmark { font-size: 96px; }
  .card-front .mark-dot { width: 34px; height: 34px; }
  .card-front .society-name { margin-top: 14px; font-size: 17px; letter-spacing: 1.5px; }
  .card-back .brand {
    right: 48px;
    top: 56px;
  }
  .card-back .wordmark { font-size: 60px; }
  .card-back .mark-dot { width: 22px; height: 22px; }
  .card-back .society-name { margin-top: 9px; font-size: 10.5px; letter-spacing: 0.8px; }
  .accent-bar {
    position: absolute;
    left: 22px;
    top: 160px;
    width: 18px;
    height: 70px;
    background: var(--navy);
  }
  .holder {
    position: absolute;
    left: 66px;
    top: 166px;
  }
  .holder-name {
    font-family: "Montserrat", Arial, sans-serif;
    font-weight: 800;
    font-size: 28px;
    letter-spacing: 2px;
    color: var(--navy);
    text-transform: uppercase;
  }
  .holder-role {
    margin-top: 4px;
    font-size: 15px;
    color: var(--ink);
  }
  .contacts {
    position: absolute;
    left: 120px;
    bottom: 50px;
    list-style: none;
    font-size: 17px;
    color: var(--ink);
  }
  .contacts li {
    display: flex;
    align-items: center;
    gap: 14px;
    height: 26px;
  }
  .contacts svg { width: 16px; height: 16px; fill: var(--navy); flex: none; }
  .contacts .address { margin-left: -4px; }
</style>
</head>
<body>
  <section class="card card-front">
    <div class="brand">
      <div class="wordmark"><span class="mark-dot"></span>KVARS</div>
      <p class="society-name">Kestrel Valley Alpine Riders Society</p>
    </div>
  </section>

  <section class="card card-back">
    <div class="brand">
      <div class="wordmark"><span class="mark-dot"></span>KVARS</div>
      <p class="society-name">Kestrel Valley Alpine Riders Society</p>
    </div>
    <div class="accent-bar"></div>
    <div class="holder">
      <p class="holder-name">Oliver Brandt</p>
      <p class="holder-role">President</p>
    </div>
    <ul class="contacts">
      <li>
        <svg viewBox="0 0 16 16" aria-hidden="true"><path d="M3 2h3l1.5 3.5-2 1.3a9 9 0 0 0 3.7 3.7l1.3-2L14 10v3a1 1 0 0 1-1 1A11 11 0 0 1 2 3a1 1 0 0 1 1-1z"/></svg>
        020 7826 1957
      </li>
      <li>
        <svg viewBox="0 0 16 16" aria-hidden="true"><path fill-rule="evenodd" d="M8 1a7 7 0 1 1 0 14A7 7 0 0 1 8 1zm-1 1.6A5.5 5.5 0 0 0 2.6 7H5c.1-1.7.8-3.3 2-4.4zM9 2.6c1.2 1.1 1.9 2.7 2 4.4h2.4A5.5 5.5 0 0 0 9 2.6zM8 3c-1 1-1.5 2.4-1.6 4h3.2C9.5 5.4 9 4 8 3zM2.6 9A5.5 5.5 0 0 0 7 13.4C5.8 12.3 5.1 10.7 5 9H2.6zm3.8 0c.1 1.6.6 3 1.6 4 1-1 1.5-2.4 1.6-4H6.4zm4.6 0c-.1 1.7-.8 3.3-2 4.4A5.5 5.5 0 0 0 13.4 9H11z"/></svg>
        oliver@kvars-club.example
      </li>
      <li>
        <svg viewBox="0 0 16 16" aria-hidden="true"><path d="M1 3h14v10H1V3zm1.5 1.2v.3L8 8.6l5.5-4.1v-.3h-11zM2.5 6v5.8h11V6L8 10.1 2.5 6z"/></svg>
        www.kvars-club.example
      </li>
      <li class="address">42 Marwick Rd, Epsom, Auckland 1051</li>
    </ul>
  </section>
</body>
</html>
```